Chatterly Design Project

I need new cover graphics for my father's chatterly page. He is running for major of our town in Puerto Rico.
Need his name on the cover: Mateo Quiñones
And the position, town and year: Alcalde Carolina 2012
As a default background color you can use the blue in the current cover graphic, or go here for color ideas http://www.adelantevecinos2012.com/indexContinuar.php
I really would like to see something that incorporates some of the pictures I have uploaded of him with people in the town, or with popular leaders. He is the guy with gray hair.
Below is the target chatterly page. Thanks
https://www.chatterly.com/mateoquinones.valderrama
Town

```html
<!DOCTYPE html>
<html lang="es">
<head>
<meta charset="utf-8">
<title>Mateo Quiñones · Alcalde Carolina 2012</title>
<link rel="stylesheet" href="https://fonts.googleapis.com/css2?family=Crimson+Text:ital,wght@1,700&family=Arimo:wght@700&display=swap">
<style>
  :root {
    --navy: #0a0a7c;
    --navy-deep: #03033f;
    --title-white: #ffffff;
    --title-shadow: rgba(0, 0, 15, 0.9);
    --year-light: #7fd4ff;
    --year-mid: #1e9cf0;
    --year-deep: #0d6fd0;
    --year-edge: #08327a;
    --gap: #d9d9d9;
  }
  * { box-sizing: border-box; margin: 0; padding: 0; }
  html, body {
    width: 1200px;
    height: 444px;
    overflow: hidden;
    background: var(--navy);
  }
  .cover {
    position: relative;
    width: 1200px;
    height: 444px;
    background: var(--navy);
    overflow: hidden;
  }
  .cover__title {
    position: absolute;
    left: 46px;
    top: 28px;
    font-family: "Crimson Text", Georgia, serif;
    font-style: italic;
    font-weight: 700;
    color: var(--title-white);
    text-shadow: 4px 5px 3px var(--title-shadow), 0 0 2px var(--navy-deep);
    line-height: 0.95;
    white-space: nowrap;
  }
  .cover__name {
    display: block;
    font-size: 80px;
  }
  .cover__office {
    display: block;
    font-size: 80px;
  }
  .cover__year {
    position: absolute;
    left: 578px;
    top: 28px;
    writing-mode: vertical-rl;
    font-family: "Arimo", Arial, sans-serif;
    font-weight: 700;
    font-size: 138px;
    letter-spacing: 16px;
    line-height: 1;
    color: var(--year-mid);
    background: linear-gradient(90deg, var(--year-light) 0%, var(--year-mid) 40%, var(--year-deep) 100%);
    -webkit-background-clip: text;
    background-clip: text;
    -webkit-text-fill-color: transparent;
    -webkit-text-stroke: 2px var(--year-edge);
  }
  .gallery {
    position: absolute;
    left: 728px;
    top: 0;
    width: 472px;
    height: 444px;
    display: grid;
    grid-template-columns: 237px 231px;
    grid-template-rows: 219px 221px;
    gap: 4px;
    background: var(--gap);
  }
  .gallery__photo { width: 100%; height: 100%; }
  .gallery__photo--hallway { background: linear-gradient(180deg, #6e6452 0%, #8b93a6 50%, #4a4640 100%); }
  .gallery__photo--porch { background: linear-gradient(180deg, #d4cdbd 0%, #e4e4ec 45%, #2f6e6a 100%); }
  .gallery__photo--rally { background: linear-gradient(180deg, #3a2a5e 0%, #8c7a62 50%, #e8e6e0 100%); }
  .gallery__photo--street { background: linear-gradient(180deg, #2c5a1e 0%, #8a6a58 45%, #8fa8cc 100%); }
</style>
</head>
<body>
  <main class="cover">
    <h1 class="cover__title">
      <span class="cover__name">Mateo Quiñones</span>
      <span class="cover__office">Alcalde Carolina</span>
    </h1>
    <div class="cover__year">2012</div>
    <section class="gallery">
      <div class="gallery__photo gallery__photo--hallway" role="img" aria-label="Photo: the candidate standing with an elderly neighbor in a hallway"></div>
      <div class="gallery__photo gallery__photo--porch" role="img" aria-label="Photo: the candidate giving a thumbs up beside a seated elderly woman on a porch"></div>
      <div class="gallery__photo gallery__photo--rally" role="img" aria-label="Photo: the candidate greeting a community leader at a rally"></div>
      <div class="gallery__photo gallery__photo--street" role="img" aria-label="Photo: the candidate with a group of town residents under a tree"></div>
    </section>
  </main>
</body>
</html>
```